Tolmira is a sparkling water from the Caucasian mountains.

Target Market(s)

High-end consumers

Colors

Designer to choose colors to be used in the design.

Requirements
Must have
• Sense of water from the mountines
Nice to have
• Sense of beign healing water

```html
<!DOCTYPE html>
<html lang="en">
<head>
<meta charset="utf-8">
<title>Tolmira Sparkling Water – Label</title>
<link href="https://fonts.googleapis.com/css2?family=Lato:wght@400;700&display=swap" rel="stylesheet">
<style>
  :root {
    --page-bg: #ffffff;
    --band-light: #e9e9ea;
    --band-mid: #d6d6d8;
    --band-dark: #c4c4c7;
    --seal-center: #ffffff;
    --seal-mid: #f7f6fb;
    --seal-edge: #d9d3ee;
    --brand-navy: #2c2f7a;
    --origin-red: #e0201f;
    --product-purple: #3f2a5e;
  }
  * { margin: 0; padding: 0; box-sizing: border-box; }
  html, body {
    width: 789px;
    height: 1200px;
    overflow: hidden;
    background: var(--page-bg);
  }
  .canvas {
    position: relative;
    width: 789px;
    height: 1200px;
    display: flex;
    align-items: center;
    justify-content: center;
  }
  .label-band {
    position: relative;
    width: 789px;
    height: 590px;
    overflow: hidden;
    background: linear-gradient(90deg, var(--band-dark) 0%, var(--band-light) 18%, var(--band-mid) 50%, var(--band-light) 82%, var(--band-dark) 100%);
  }
  .label-seal {
    position: absolute;
    left: 50%;
    top: 50%;
    width: 700px;
    height: 700px;
    transform: translate(-50%, -50%);
    border-radius: 50%;
    background: radial-gradient(circle at 50% 50%, var(--seal-center) 0%, var(--seal-mid) 62%, var(--seal-edge) 100%);
  }
  .label-text {
    position: absolute;
    inset: 0;
    display: flex;
    flex-direction: column;
    align-items: center;
    justify-content: center;
    font-family: "Lato", sans-serif;
    text-align: center;
  }
  .brand-name {
    font-weight: 400;
    font-size: 150px;
    line-height: 1;
    letter-spacing: 4px;
    color: var(--brand-navy);
    margin-top: 40px;
  }
  .origin-line {
    font-weight: 400;
    font-size: 44px;
    color: var(--origin-red);
    margin-top: 30px;
  }
  .product-line {
    font-weight: 400;
    font-size: 56px;
    letter-spacing: 2px;
    color: var(--product-purple);
    margin-top: 14px;
  }
</style>
</head>
<body>
  <main class="canvas">
    <section class="label-band">
      <div class="label-seal"></div>
      <div class="label-text">
        <h1 class="brand-name">tolmira</h1>
        <p class="origin-line">Caucasian mountains</p>
        <p class="product-line">SPARKLING WATER</p>
      </div>
    </section>
  </main>
</body>
</html>
```